Project Planning & Communication Process

Need a PowerPoint slide that illustrates our project planning and communication cycle. Our company has key meetings, and key communication vehicles (like emails and follow up tools) that we use to ensure our frontline staff are prepared to execute the new project successfully. This document needs to call out how the different components, like the meetings and emails, work together (like a flow chart), so someone who needs to use this process will understand what they should do. The slide needs to be simple yet comprehensive enough to guide someone through the details. I don't want it overwhelming. The primary focus is the process, not the details.

Use the color pallette included within the slide (shades of blue and gray, and black). This is for an insurance company (www.harborquill.com). Use this as a reference for the look and feel.

I have attached a sample slide of the flow chart process.

Click here if you cannot access the file. https://www.filecrate.example/s/q8wz2mbt7ypnc4r/Communcation_Methods_V1.pptx

If you are not able to see the uploaded slide.  Please send me your email address and I will send the slide to you directly. 

ISince I'm not able to upload the reference ppt file, 've uploaded the slide at FileCrate.  Please click here to access.
https://www.filecrate.example/s/q8wz2mbt7ypnc4r/Communcation_Methods_V1.pptx

Reason: extending one more day for designers to make last minute updates.

Target Market(s)

Vice Presidents and project managers/business partners within the organization.

Industry/Entity Type

Communication

Font styles to use
Sans Serif

Colors
3176b5

Requirements
Must have
• 1 page, color pallette assigned, be simple yet comprehensive. the focus needs to be on the process, not on the details.
Nice to have
• Doesn't have to follow the example I provided. Please feel free to approach from different ways.

```html
<!DOCTYPE html>
<html lang="en">
<head>
<meta charset="utf-8">
<title>Project Alignment &amp; Communication Process</title>
<link href="https://fonts.googleapis.com/css2?family=Arimo:wght@700&display=swap" rel="stylesheet">
<style>
  :root {
    --brand-blue: #3176b5;
    --ink: #0d0d0d;
    --tail-gray: #2a2a2a;
    --paper: #ffffff;
    --on-dark: #ffffff;
  }
  * { margin: 0; padding: 0; box-sizing: border-box; }
  html, body { width: 1200px; height: 900px; overflow: hidden; background: var(--paper); }
  body { font-family: "Arimo", Arial, sans-serif; font-weight: 700; }

  .slide { position: relative; width: 1200px; height: 900px; background: var(--paper); overflow: hidden; }

  .ribbon-tails { position: absolute; left: 0; top: 0; width: 1200px; height: 200px; }
  .title-banner {
    position: absolute; left: 246px; top: 43px; width: 733px; height: 64px;
    background: var(--paper); border: 4px dotted var(--brand-blue);
    display: flex; align-items: center; justify-content: center;
    color: var(--brand-blue); font-size: 22px; letter-spacing: 0.4px;
  }

  .phase-panel { position: absolute; top: 189px; height: 711px; background: var(--ink); }
  .phase-panel--plan { left: 0; width: 364px; }
  .phase-panel--follow { left: 833px; width: 367px; }

  .phase-frame { position: absolute; border: 5px dotted var(--brand-blue); border-bottom: none; }
  .phase-frame--plan { left: 26px; top: 257px; width: 57px; height: 643px; }
  .phase-frame--prepare { left: 439px; top: 240px; width: 61px; height: 660px; }
  .phase-frame--follow { left: 854px; top: 240px; width: 62px; height: 660px; }

  .phase-number {
    position: absolute; font-size: 178px; line-height: 1; color: var(--brand-blue);
  }
  .phase-number--plan { left: 10px; top: 320px; }
  .phase-number--prepare { left: 424px; top: 306px; }
  .phase-number--follow { left: 838px; top: 320px; }

  .phase-label {
    position: absolute; writing-mode: vertical-rl; transform: rotate(180deg);
    font-size: 21px; letter-spacing: 0.6px; white-space: nowrap;
  }
  .phase-label--plan { left: 50px; top: 493px; color: var(--on-dark); }
  .phase-label--prepare { left: 468px; top: 484px; color: var(--ink); }
  .phase-label--follow { left: 880px; top: 479px; color: var(--on-dark); }

  .timing-arrow { position: absolute; }
  .timing-arrow svg { display: block; }
  .timing-arrow__text {
    position: absolute; left: 0; color: var(--on-dark); font-size: 19.5px; white-space: nowrap;
  }

  .step-list { position: absolute; list-style: none; font-size: 19.5px; line-height: 24px; }
  .step-list li { position: absolute; left: 0; white-space: nowrap; }
  .step-list--plan { left: 108px; top: 0; color: var(--on-dark); }
  .step-list--prepare { left: 521px; top: 0; color: var(--ink); }

  .follow-list { position: absolute; left: 963px; top: 471px; color: var(--on-dark); font-size: 31px; line-height: 34px; list-style: none; }
  .follow-list li + li { margin-top: 34px; }
</style>
</head>
<body>
<main class="slide">

  <svg class="ribbon-tails" viewBox="0 0 1200 200" aria-hidden="true">
    <g class="ribbon-tail">
      <path d="M183,100 Q330,108 493,124 L493,157 Q350,158 236,176 Q268,138 183,100 Z" fill="var(--tail-gray)"/>
      <path d="M300,138 L493,126 L493,160 Z" fill="var(--brand-blue)"/>
    </g>
    <g class="ribbon-tail" transform="translate(1200,0) scale(-1,1)">
      <path d="M183,100 Q330,108 493,124 L493,157 Q350,158 236,176 Q268,138 183,100 Z" fill="var(--tail-gray)"/>
      <path d="M300,138 L493,126 L493,160 Z" fill="var(--brand-blue)"/>
    </g>
  </svg>

  <h1 class="title-banner">PROJECT ALIGNMENT &amp; COMMUNICATION PROCESS</h1>

  <div class="phase-panel phase-panel--plan"></div>
  <div class="phase-panel phase-panel--follow"></div>

  <!-- Phase 1 -->
  <div class="phase-frame phase-frame--plan"></div>
  <div class="phase-number phase-number--plan">1</div>
  <div class="phase-label phase-label--plan">PLANNING &amp; DESIGN PHASE</div>

  <div class="timing-arrow" style="left:107px; top:221px;">
    <svg width="257" height="115" viewBox="0 0 257 115"><path d="M0,29 H180 V0 L257,57.5 L180,115 V86 H0 Z" fill="var(--brand-blue)"/></svg>
    <span class="timing-arrow__text" style="top:45px; left:3px;">3+ MONTHS OUT</span>
  </div>
  <div class="timing-arrow" style="left:107px; top:550px;">
    <svg width="257" height="107" viewBox="0 0 257 107"><path d="M0,24 H180 V0 L257,53.5 L180,107 V81 H0 Z" fill="var(--brand-blue)"/></svg>
    <span class="timing-arrow__text" style="top:41px; left:3px;">2 + MONTHS OUT</span>
  </div>

  <ul class="step-list step-list--plan">
    <li style="top:317px;">NEW<br>PROJECT</li>
    <li style="top:393px;">IDENTIFIED<br>GOVERNANCE<br>MEETING</li>
    <li style="top:493px;">SEPARATE PROJECT<br>MEETINGS AS<br>NEEDED</li>
    <li style="top:669px;">GOVERNANCE<br>MEETING</li>
    <li style="top:743px;">WEEKLY CENTER<br>LEADER<br>MEETING</li>
    <li style="top:843px;">FIELD ADVISORY<br>PANEL</li>
  </ul>

  <!-- Phase 2 -->
  <div class="phase-frame phase-frame--prepare"></div>
  <div class="phase-number phase-number--prepare">2</div>
  <div class="phase-label phase-label--prepare">PREPARE PHASE</div>

  <div class="timing-arrow" style="left:517px; top:343px;">
    <svg width="262" height="114" viewBox="0 0 262 114"><path d="M0,28 H172 V0 L262,57 L172,114 V86 H0 Z" fill="var(--brand-blue)"/></svg>
    <span class="timing-arrow__text" style="top:44px; left:4px;">1 MONTH OUT</span>
  </div>
  <div class="timing-arrow" style="left:517px; top:564px;">
    <svg width="254" height="115" viewBox="0 0 254 115"><path d="M0,32 H165 V0 L254,57.5 L165,115 V89 H0 Z" fill="var(--brand-blue)"/></svg>
    <span class="timing-arrow__text" style="top:47px; left:4px;">1 WEEK OUT</span>
  </div>

  <ul class="step-list step-list--prepare">
    <li style="top:464px;">WEEKLY CENTER<br>LEADER<br>MEETING</li>
    <li style="top:664px;">MONDAY<br>MEMO</li>
    <li style="top:740px;">DAILY<br>DIGEST</li>
  </ul>

  <!-- Phase 3 -->
  <div class="phase-frame phase-frame--follow"></div>
  <div class="phase-number phase-number--follow">3</div>
  <div class="phase-label phase-label--follow">FOLLOW UP &amp; EVALUATE</div>

  <ul class="follow-list">
    <li>FOLLOW<br>UP<br>GUIDE</li>
    <li>POST<br>LAUNCH</li>
  </ul>

</main>
</body>
</html>
```